Ironvale Holdings Business card

We need a an amazing matte black and gold card! W are a finance investing company so we want something that's eye catching and sleek. We want it to be attractive and sleek and represent money. Heck with would like the letters and lgo to be printed as 24k gold one day. We have the logo added so please use the color scheme with the logo and have that beautifully placed on one side.

Target Market(s)

Investors of all ages

Industry/Entity Type

Financial

Contact Information for Business Card

Black and matte with gold lettering follow logo colrs please.

Font styles to use
Other font styles liked:
• you decide

Colors

Designer to choose colors to be used in the design.

Requirements
Must have
• Matte Black and Gold, logo on one side. job title and name , website, phone number and email address on the other side
Nice to have
• Matte black and crisp finish to attract investors
Should not have
• playful, very professional!

```html
<!DOCTYPE html>
<html lang="en">
<head>
<meta charset="UTF-8">
<title>Ironvale Holdings Business Card</title>
<link href="https://fonts.googleapis.com/css2?family=Cinzel:wght@500&family=Mulish:wght@400&display=swap" rel="stylesheet">
<style>
  :root {
    --backdrop: #2b2c2f;
    --card-black: #1a1a1a;
    --gold: #c9a62c;
    --white: #f2f2f2;
  }
  * { margin: 0; padding: 0; box-sizing: border-box; }
  html, body {
    width: 1200px;
    height: 900px;
    overflow: hidden;
    background: var(--backdrop);
  }
  .canvas {
    position: relative;
    width: 1200px;
    height: 900px;
    display: flex;
    flex-direction: column;
    align-items: center;
    justify-content: center;
    gap: 32px;
  }
  .card {
    width: 660px;
    height: 378px;
    background: var(--card-black);
    box-shadow: 0 10px 28px rgba(0,0,0,0.45);
    position: relative;
  }
  .card-front {
    display: flex;
    align-items: center;
    justify-content: center;
  }
  .brand-name {
    font-family: "Cinzel", serif;
    font-weight: 500;
    font-size: 34px;
    letter-spacing: 0.06em;
    color: var(--gold);
    text-transform: uppercase;
  }
  .card-back {
    display: flex;
    align-items: center;
    justify-content: center;
    padding-top: 6px;
  }
  .identity {
    text-align: right;
    padding-right: 22px;
  }
  .person-name {
    font-family: "Cinzel", serif;
    font-weight: 500;
    font-size: 30px;
    letter-spacing: 0.03em;
    color: var(--gold);
    line-height: 1.1;
  }
  .job-title {
    font-family: "Mulish", sans-serif;
    font-size: 15px;
    color: var(--white);
    margin-top: 4px;
  }
  .divider {
    width: 2px;
    height: 70px;
    background: var(--white);
  }
  .contacts {
    list-style: none;
    padding-left: 22px;
    display: flex;
    flex-direction: column;
    gap: 6px;
  }
  .contact-item {
    display: flex;
    align-items: center;
    gap: 14px;
    font-family: "Mulish", sans-serif;
    font-size: 15px;
    color: var(--white);
  }
  .contact-icon {
    width: 14px;
    height: 14px;
    flex: none;
  }
</style>
</head>
<body>
  <main class="canvas">
    <section class="card card-front" aria-label="Card front">
      <h1 class="brand-name">Ironvale Holdings</h1>
    </section>

    <section class="card card-back" aria-label="Card back">
      <div class="identity">
        <p class="person-name">DANIEL HART</p>
        <p class="job-title">Operational Manager</p>
      </div>
      <div class="divider"></div>
      <ul class="contacts">
        <li class="contact-item">
          <svg class="contact-icon" viewBox="0 0 14 14" aria-hidden="true">
            <rect x="3.5" y="1" width="7" height="12" rx="1.2" fill="none" stroke="#c9a62c" stroke-width="1.4"/>
            <line x1="6" y1="11" x2="8" y2="11" stroke="#c9a62c" stroke-width="1.2"/>
          </svg>
          <span>+999 5550 0142</span>
        </li>
        <li class="contact-item">
          <svg class="contact-icon" viewBox="0 0 14 14" aria-hidden="true">
            <rect x="1" y="3" width="12" height="8.5" fill="#c9a62c"/>
            <polyline points="1,3 7,8 13,3" fill="none" stroke="#1a1a1a" stroke-width="1.2"/>
          </svg>
          <span>daniel.hart@ironvale.com</span>
        </li>
        <li class="contact-item">
          <svg class="contact-icon" viewBox="0 0 14 14" aria-hidden="true">
            <circle cx="7" cy="7" r="6" fill="none" stroke="#c9a62c" stroke-width="1.3"/>
            <ellipse cx="7" cy="7" rx="2.6" ry="6" fill="none" stroke="#c9a62c" stroke-width="1.1"/>
            <line x1="1" y1="7" x2="13" y2="7" stroke="#c9a62c" stroke-width="1.1"/>
          </svg>
          <span>www.ironvale.com</span>
        </li>
      </ul>
    </section>
  </main>
</body>
</html>
```